Logo and metal business card design

Updated added my current logo which focus needs to be concentrated on. Have to have the new logo before the card. Company name is The Halden Crest, LLC

Update: Reminder this is a Logo and business card design. I want the logo to be “HaldenC” in a unique professional design that says secure, insurance, financial.

The G needs to be a P in the cut out

Update: the top two images have design on the metal which I am looking for

New black metal business cards. And HaldenC.com logo that will go on the card. This will be a cut out design in the metal. Featuring “HaldenC.com as the main cutout. Like the idea of .com to be separate or smaller and possible color. Looking for unique HaldenC font design and a surrounding design per the examples below. Halden and G need to be different and the G a specific designing the mesh like the attached with the V in the mesh. But card side ways.. so mesh on right side of card with a G and .com in lower corner or where it fits Also looking to add my main info on the back side of the card. Derek M. Cell contact@mailbox-example.net We are an commercial insurance broker specializing in program business.

Need more time not enough entry’s and they are all the same.. I’m suppose to get 75 plus and not 20 that are the exact same from artist??? Need more submissions to compare. I committed my money so I do not want a refund I want more submissions from different artist

Designs look the same

Target Market(s)

Insurance for the Restaurant industry

Industry/Entity Type

Insurance Broker

Contact Information for Business Card

New black metal business cards. And HaldenC.com logo that will go on the card. This will be a cut out design in the metal. Featuring “HaldenC.com as the main cutout. Like the idea of .com to be separate or smaller and possible color. Looking for unique HaldenC font design and a surrounding design per the examples below. Halden and G need to be different and the G a specific designing the mesh like the attached with the V in the mesh. But card side ways.. so mesh on right side of card with a G and .com in lower corner or where it fits
Also looking to add my main info on the back side of the card.
Derek M.
Cell
contact@mailbox-example.net

We are an commercial insurance broker specializing in program business.

Logo Text

HaldenC.com

Font styles to use
Decorative
Script
Other font styles liked:

Requirements
Must have
• Must have Halden and G distinctively different
Nice to have
• On flat parts I want texture on top of card

```html
<!DOCTYPE html>
<html lang="en">
<head>
<meta charset="utf-8">
<title>HaldenC Business Card</title>
<link rel="stylesheet" href="https://fonts.googleapis.com/css2?family=Work+Sans:wght@400;500;700&display=swap">
<style>
  :root {
    --backdrop: #141414;
    --card: #1c1c1c;
    --card-edge: #262626;
    --foil: #c9c9c9;
    --foil-soft: #a9a9a9;
    --divider: #8a8a8a;
  }
  * { margin: 0; padding: 0; box-sizing: border-box; }
  html, body {
    width: 1200px;
    height: 900px;
    overflow: hidden;
    background: var(--backdrop);
    font-family: "Work Sans", sans-serif;
  }
  .canvas {
    width: 1200px;
    height: 900px;
    display: flex;
    flex-direction: column;
    align-items: center;
    justify-content: center;
    gap: 50px;
  }
  .card {
    width: 700px;
    height: 380px;
    background: var(--card);
    border: 1px solid var(--card-edge);
    position: relative;
  }
  .card--front {
    display: flex;
    align-items: center;
    justify-content: center;
  }
  .brand {
    display: flex;
    align-items: center;
    gap: 16px;
    color: var(--foil);
    font-weight: 700;
    letter-spacing: 1px;
  }
  .brand__square {
    background: var(--foil);
  }
  .card--front .brand { font-size: 74px; }
  .card--front .brand__square { width: 62px; height: 62px; }
  .card--back {
    display: flex;
    align-items: center;
    padding: 0 0 0 46px;
  }
  .card--back .brand { font-size: 58px; gap: 12px; width: 360px; }
  .card--back .brand__square { width: 48px; height: 48px; }
  .divider {
    width: 2px;
    height: 210px;
    background: var(--divider);
    margin: 0 34px 0 8px;
  }
  .contact { color: var(--foil-soft); }
  .contact__name {
    font-size: 20px;
    font-weight: 500;
    letter-spacing: 1px;
    color: var(--foil);
  }
  .contact__role { font-size: 15px; margin-bottom: 22px; }
  .contact__address { font-size: 15px; line-height: 1.45; letter-spacing: 1px; margin-bottom: 18px; }
  .contact__list { list-style: none; font-size: 16px; letter-spacing: 1px; line-height: 1.75; }
  .contact__list li { display: flex; align-items: center; gap: 10px; }
  .contact__icon { width: 12px; height: 12px; flex: none; }
</style>
</head>
<body>
<main class="canvas">
  <section class="card card--front" aria-label="Card front">
    <div class="brand"><span class="brand__square"></span><span class="brand__name">HaldenC</span></div>
  </section>

  <section class="card card--back" aria-label="Card back">
    <div class="brand"><span class="brand__square"></span><span class="brand__name">HaldenC</span></div>
    <div class="divider"></div>
    <div class="contact">
      <p class="contact__name">ADRIAN VELL</p>
      <p class="contact__role">Director</p>
      <p class="contact__address">48b Marlow Lane,<br>Ashford, NZ, 7024</p>
      <ul class="contact__list">
        <li>
          <svg class="contact__icon" viewBox="0 0 12 12" aria-hidden="true"><path d="M2.5 1 L4.5 1 L5.2 3.6 L4 4.6 Q5.2 7 7.4 8 L8.4 6.8 L11 7.5 L11 9.5 Q10 11 8.5 11 Q2.5 10 1 3.5 Q1 2 2.5 1 Z" fill="var(--foil-soft)"/></svg>
          (555) 013-2748
        </li>
        <li>
          <svg class="contact__icon" viewBox="0 0 12 12" aria-hidden="true"><rect x="0.8" y="2.3" width="10.4" height="7.4" fill="none" stroke="var(--foil-soft)" stroke-width="1.2"/><path d="M1 2.6 L6 6.5 L11 2.6" fill="none" stroke="var(--foil-soft)" stroke-width="1.2"/></svg>
          info@HaldenC.com
        </li>
        <li>
          <svg class="contact__icon" viewBox="0 0 12 12" aria-hidden="true"><circle cx="6" cy="6" r="5" fill="none" stroke="var(--foil-soft)" stroke-width="1.1"/><ellipse cx="6" cy="6" rx="2.2" ry="5" fill="none" stroke="var(--foil-soft)" stroke-width="1"/><path d="M1 6 H11" stroke="var(--foil-soft)" stroke-width="1"/></svg>
          www.HaldenC.com
        </li>
      </ul>
    </div>
  </section>
</main>
</body>
</html>
```